New Sticker Design Project

Hello, Thank you for the great design of the tape. I would like to hire you to create another design to match the tape for the side of the box. 4" X 6"
Text: Perishable, Living Food as Medicine, Please Keep Cold, Do Not Delay, Quick Delivery Necessary, Place in Refrigerator Immediately upon Delivery
With symbols for Cold, and time-sensitive. Could use all caps if the design looks good. Same text font and color scheme to match the look of the tape. Logo if space. This needs to stand out on the shipping box which is brown boxes. Thanks again. !
Target Market(s)
Shipping box informational Sticker Outside
Requirements
Must have
- Similar matching look to the tape. The word PERISHABLE needs to be dominate!
Nice to have
- bold easy to read eye catching information for Parzo and customer
Should not have
- Clutter

```html
<!DOCTYPE html>
<html lang="en">
<head>
<meta charset="utf-8">
<title>Verda Spirulina – Shipping Sticker</title>
<link rel="stylesheet" href="https://fonts.googleapis.com/css2?family=Barlow+Condensed:wght@500&family=League+Spartan:wght@700&display=swap">
<style>
  :root {
    --page: #f9fcfc;
    --ink: #2e2e2e;
    --black: #111111;
    --teal: #2f8f7e;
  }
  html, body { margin: 0; padding: 0; overflow: hidden; }
  body { width: 967px; height: 1200px; background: var(--page); position: relative; }
  .sticker {
    position: absolute; left: 53px; top: 313px; width: 860px; height: 573px;
    box-sizing: border-box; border: 16px solid var(--ink); background: var(--page);
  }
  .brand-mark {
    position: absolute; left: 186px; top: 46px; width: 84px; height: 84px;
    border-radius: 50%; background: var(--teal);
  }
  .brand-name {
    position: absolute; left: 300px; top: 34px; width: 380px; margin: 0;
    font-family: "League Spartan", sans-serif; font-weight: 700; font-size: 64px;
    line-height: 60px; color: var(--ink); text-align: center; text-transform: uppercase;
  }
  .tagline {
    position: absolute; left: 300px; top: 150px; width: 380px; margin: 0;
    font-family: "Barlow Condensed", sans-serif; font-weight: 500; font-size: 16px;
    letter-spacing: 3px; line-height: 18px; text-align: center; color: var(--ink);
    text-transform: uppercase;
  }
  .notice { position: absolute; width: 260px; text-align: center; }
  .notice .icon-box {
    display: flex; align-items: flex-end; justify-content: center;
  }
  .row-1 .icon-box { height: 124px; }
  .row-2 .icon-box { height: 100px; }
  .notice .label {
    margin: 8px 0 0; font-family: "Barlow Condensed", sans-serif; font-weight: 500;
    font-size: 24px; line-height: 26px; color: var(--ink); text-transform: uppercase;
  }
  .col-1 { left: 30px; } .col-2 { left: 258px; } .col-3 { left: 513px; }
  .row-1 { top: 190px; } .row-2 { top: 364px; }
  .perishable-art {
    width: 96px; height: 117px;
    background: linear-gradient(180deg, #3a3a3a, #1a1a1a);
  }
</style>
</head>
<body>
<main class="sticker">
  <div class="brand-mark"></div>
  <h1 class="brand-name">Verda<br>Spirulina</h1>
  <p class="tagline">Fresh from the pond</p>

  <section class="notice col-1 row-1">
    <div class="icon-box">
      <div class="perishable-art" role="img" aria-label="Perishable goods emblem with hourglass framed by food items"></div>
    </div>
    <p class="label">Perishable</p>
  </section>

  <section class="notice col-2 row-1">
    <div class="icon-box">
      <svg width="124" height="124" viewBox="0 0 124 124" aria-hidden="true">
        <circle cx="60" cy="60" r="55" fill="none" stroke="var(--black)" stroke-width="8"/>
        <circle cx="60" cy="60" r="42" fill="none" stroke="var(--black)" stroke-width="4"/>
        <path d="M60 24 V62 H88" fill="none" stroke="var(--black)" stroke-width="6"/>
        <g stroke="var(--black)" stroke-width="4">
          <path d="M60 20v6M20 60h6M32 32l4 4M32 88l4-4"/>
        </g>
        <circle cx="93" cy="93" r="27" fill="var(--page)" stroke="var(--black)" stroke-width="8"/>
        <path d="M93 78v17" stroke="var(--black)" stroke-width="7" stroke-linecap="round"/>
        <circle cx="93" cy="106" r="4" fill="var(--black)"/>
      </svg>
    </div>
    <p class="label">Do not delay</p>
  </section>

  <section class="notice col-3 row-1">
    <div class="icon-box">
      <svg width="110" height="118" viewBox="-56 -61 112 122" aria-hidden="true">
        <g stroke="var(--black)" stroke-width="9" stroke-linecap="round" fill="none">
          <g id="arm"><path d="M0 -10 V-54 M0 -34 L-14 -48 M0 -34 L14 -48"/></g>
          <use href="#arm" transform="rotate(60)"/>
          <use href="#arm" transform="rotate(120)"/>
          <use href="#arm" transform="rotate(180)"/>
          <use href="#arm" transform="rotate(240)"/>
          <use href="#arm" transform="rotate(300)"/>
        </g>
      </svg>
    </div>
    <p class="label">Please keep cold</p>
  </section>

  <section class="notice col-1 row-2">
    <div class="icon-box">
      <svg width="96" height="96" viewBox="0 0 96 96" aria-hidden="true">
        <path d="M4 4v20q0 8 8 8h6v62h6V32h6q8 0 8-8V4h-5v18h-4V4h-5v18h-5V4h-5v18H9V4z" fill="var(--black)"/>
        <path d="M84 2q10 10 10 40v12h-4v40h-6z" fill="var(--black)"/>
        <path d="M52 84 L26 60 Q14 48 24 38 Q36 30 52 44 Q68 30 80 38 Q90 48 78 60z" fill="var(--black)"/>
        <path d="M30 58h10l5-9 6 16 5-10h14" fill="none" stroke="var(--page)" stroke-width="3"/>
      </svg>
    </div>
    <p class="label">Living food<br>as medicine</p>
  </section>

  <section class="notice col-2 row-2">
    <div class="icon-box">
      <svg width="122" height="76" viewBox="0 4 122 82" aria-hidden="true">
        <rect x="14" y="10" width="72" height="56" rx="6" fill="var(--black)"/>
        <path d="M88 22h16l16 22v22H88z" fill="var(--black)"/>
        <path d="M93 27h9l10 14H93z" fill="var(--page)"/>
        <g fill="var(--black)"><rect x="0" y="22" width="26" height="6" rx="3"/><rect x="6" y="36" width="22" height="6" rx="3"/><rect x="2" y="50" width="20" height="6" rx="3"/></g>
        <circle cx="34" cy="72" r="12" fill="var(--black)" stroke="var(--page)" stroke-width="4"/>
        <circle cx="100" cy="72" r="12" fill="var(--black)" stroke="var(--page)" stroke-width="4"/>
      </svg>
    </div>
    <p class="label">Quick delivery<br>necessary</p>
  </section>

  <section class="notice col-3 row-2">
    <div class="icon-box">
      <svg width="46" height="98" viewBox="0 0 48 98" aria-hidden="true">
        <g fill="none" stroke="var(--black)" stroke-width="3">
          <rect x="2" y="2" width="44" height="94"/>
          <path d="M2 28h44M8 8v14M8 36v24M6 96 10 90h28l4 6"/>
        </g>
      </svg>
    </div>
    <p class="label">Place in refrigerator<br>immediately upon delivery</p>
  </section>
</main>
</body>
</html>
```